CSS Template Layout

We are looking for a page design template that we can update our site. Here are the requirements.

We need a header image across the top and three columns below. Layout should be controlled by css, not tables.

This is for a landscape/snow removal directory. A generic layout for overall size can be found at www.brindlemeadowyards.example Images should relate to lawns/landscaping/snow removal.

We do not have a logo at this time, so we will simply be using a font with the site name. The site should be colorful and inviting, it should feel fresh and clean. These are landscapers and they groom the beauty found in nature.

Do not hesitate to ask questions or bounce ideas off of us.
Updates

Project Deadline Extended
Reason: We are sorry but we need to extend the deadline, we inadvertently deadlined on a Saturday and will not be in the office. We have internally worked out our schedules to meet next thursday. On the plus side, we are guaranteeing payment based on the two designs submitted already.

```html
<!DOCTYPE html>
<html lang="en">
<head>
<meta charset="utf-8">
<title>Brindle Meadow Yards</title>
<link href="https://fonts.googleapis.com/css2?family=Open+Sans:wght@400;600;700&family=Roboto+Condensed:wght@400&display=swap" rel="stylesheet">
<style>
:root{
  --green:#8cbf26;
  --green-dark:#6f9e14;
  --ink:#333;
  --line:#e2e2e2;
  --band:#f5f5f5;
  --footer:#202020;
  --footer-text:#cfcfcf;
  --footer-rule:#555;
}
*{margin:0;padding:0;box-sizing:border-box}
html,body{width:821px;height:1200px;overflow:hidden;background:#fff}
body{font-family:"Open Sans",Arial,sans-serif;color:var(--ink);position:relative}
a{color:inherit;text-decoration:none}

.topbar{height:31px;border-top:3px solid var(--green);border-bottom:1px solid #ececec;font-size:8px;color:#555;position:relative}
.topbar .item{position:absolute;top:8px;display:flex;align-items:center;gap:6px;white-space:nowrap}
.topbar svg{width:10px;height:10px;fill:#555;flex:none}

.masthead{height:52px;position:relative}
.site-name{position:absolute;left:77px;top:13px;font-family:"Roboto Condensed",Arial,sans-serif;font-size:22px;color:#222;letter-spacing:.2px;text-transform:uppercase}
.nav{position:absolute;top:21px;right:76px;display:flex;gap:26px;font-size:9px;text-transform:uppercase;color:#333}
.nav .active{color:var(--green-dark)}

.hero{position:absolute;top:83px;left:0;width:821px;height:266px;border-bottom:3px solid #ddd;
  background:
    radial-gradient(ellipse 130px 90px at 450px 150px,rgba(214,170,30,.75),transparent 70%),
    radial-gradient(ellipse 200px 70px at 300px 220px,rgba(160,155,145,.8),transparent 70%),
    radial-gradient(ellipse 130px 80px at 680px 230px,rgba(165,190,190,.75),transparent 70%),
    radial-gradient(ellipse 90px 60px at 110px 250px,rgba(120,90,160,.55),transparent 70%),
    linear-gradient(180deg,#2c4a1c 0%,#3f6126 50%,#4d6a30 100%)}
.hero h1{position:absolute;left:78px;top:87px;font-size:29px;font-weight:700;color:#fff;letter-spacing:.2px}
.hero p{position:absolute;left:78px;top:127px;font-size:13px;line-height:17px;color:#fff}
.btn{display:inline-block;background:var(--green);color:#fff;font-weight:700;font-size:10px;text-transform:uppercase;text-align:center}
.hero .btn{position:absolute;left:76px;top:173px;width:104px;height:26px;line-height:26px}
.hero .arrow{position:absolute;top:124px;width:18px;height:24px}
.hero .dots{position:absolute;left:391px;top:236px;display:flex;gap:5px}
.hero .dots i{width:9px;height:9px;border-radius:50%;background:rgba(255,255,255,.5)}
.hero .dots i:first-child{background:#fff}

.services{position:absolute;top:373px;left:79px;display:flex;gap:33px}
.service{width:199px}
.service .thumb{height:89px;border:4px solid #e6e6e6}
.service h2{font-size:12px;font-weight:400;margin:12px 0 5px 2px;color:#333}
.service p{font-size:7.5px;line-height:14px;color:#555;margin-left:2px}
.service .more{display:block;font-size:7.5px;color:var(--green-dark);margin:16px 0 0 1px}

.featured{position:absolute;top:596px;left:75px;width:670px}
.featured h2{font-size:18px;font-weight:400;color:#333;padding-bottom:6px;border-bottom:1px solid var(--line)}
.featured .pager{position:absolute;right:2px;top:8px;display:flex;gap:2px}
.featured .pager span{width:16px;height:15px;display:block}
.partners{display:flex;gap:11px;margin-top:16px}
.partner{width:160px;height:78px;border:1px solid #ddd;display:flex;align-items:center;justify-content:center;gap:7px;font-size:13px;font-weight:700;color:#3d6b1c}
.partner i{width:12px;height:12px;background:#3d6b1c;border-radius:50%}

.cta{position:absolute;top:734px;left:0;width:821px;height:87px;background:var(--band)}
.cta p{position:absolute;left:86px;top:25px;font-size:12.5px;line-height:16px;color:#333;width:500px}
.cta .btn{position:absolute;left:618px;top:29px;width:103px;height:27px;line-height:27px}

.footer{position:absolute;top:873px;left:0;width:821px;height:327px;background:var(--footer);border-top:3px solid #d6d6d6}
.footer .col{position:absolute;top:34px;width:157px}
.footer h3{font-size:8.5px;font-weight:700;color:#fff;text-transform:uppercase;padding-bottom:6px;border-bottom:3px solid #444}
.footer ul{list-style:none;margin-top:18px}
.footer li{font-size:7.5px;color:var(--footer-text);height:24.5px;line-height:17px;border-bottom:1px dotted var(--footer-rule);padding-left:19px;position:relative}
.footer li:before{content:"";position:absolute;left:6px;top:6px;border-left:4px solid #777;border-top:3px solid transparent;border-bottom:3px solid transparent}
.social{display:grid;grid-template-columns:repeat(4,14px);gap:13px 15px;margin-top:20px;margin-left:4px}
.social i{width:11px;height:11px;background:#e4e4e4;border-radius:2px}
.contact-list{margin-top:10px}
.contact-list div{display:flex;align-items:center;gap:12px;font-size:7.5px;color:var(--footer-text);height:21px;margin-left:4px}
.contact-list svg{width:10px;height:10px;fill:#777}
.copyright{position:absolute;left:77px;right:76px;top:285px;border-top:1px solid #333;padding-top:16px;font-size:7.5px;color:var(--footer-text)}
</style>
</head>
<body>

<header>
  <div class="topbar">
    <span class="item" style="left:76px">
      <svg viewBox="0 0 10 10"><path d="M0 2h10v6H0z" fill="#555"/><path d="M0.5 2.5l4.5 2.7 4.5-2.7" fill="none" stroke="#fff" stroke-width=".8"/></svg>
      hello@brindlemeadowyards.example
    </span>
    <span class="item" style="left:262px">
      <svg viewBox="0 0 10 10"><path d="M2 0.5l2 2-1 1.3c.7 1.4 1.8 2.5 3.2 3.2l1.3-1 2 2-1.4 1.5C5 9.2 .8 5 .5 2z"/></svg>
      (555)010-4417
    </span>
    <span class="item" style="left:646px">
      <svg viewBox="0 0 10 10"><path d="M2 4.5h6V10H2z"/><path d="M3 4.5V3a2 2 0 0 1 4 0v1.5" fill="none" stroke="#555" stroke-width="1.2"/></svg>
      Login
    </span>
    <span class="item" style="left:697px">
      <svg viewBox="0 0 10 10"><path d="M1 1h8v8H1z" fill="none" stroke="#555"/><path d="M2.5 3h5v1h-5zM2.5 5h5v1h-5zM2.5 7h3v1h-3z"/></svg>
      Register
    </span>
  </div>
  <div class="masthead">
    <div class="site-name">Brindle Meadow Yards</div>
    <nav class="nav">
      <a class="active" href="#">Home</a>
      <a href="#">Landscape Service</a>
      <a href="#">Lawn Service</a>
      <a href="#">Snow Removal Service</a>
    </nav>
  </div>
</header>

<section class="hero" role="img" aria-label="Garden path of stones and gravel lined with yellow flowers, shrubs and evergreens">
  <h1>LANDSCAPE SERVICE</h1>
  <p>A Professional Listing of Lawn Service,<br>Tree Service and Snow Removal Service Companies.</p>
  <a class="btn" href="#">Learn More</a>
  <svg class="arrow" style="left:14px" viewBox="0 0 18 24"><path d="M14 2L4 12l10 10" fill="none" stroke="#fff" stroke-width="4" opacity=".85"/></svg>
  <svg class="arrow" style="left:786px" viewBox="0 0 18 24"><path d="M4 2l10 10L4 22" fill="none" stroke="#fff" stroke-width="4" opacity=".85"/></svg>
  <div class="dots"><i></i><i></i><i></i></div>
</section>

<section class="services">
  <article class="service">
    <div class="thumb" role="img" aria-label="Sunlit lawn with a curving garden path" style="background:linear-gradient(180deg,#4a6a18 0%,#7f9c22 45%,#b5b83a 75%,#6e8a1c 100%)"></div>
    <h2>Landscape Service</h2>
    <p>We service both residential and commercial properties.<br>We take pride in our Company, and this pride reflects<br>in the properties we maintain.</p>
    <a class="more" href="#">Learn more ›</a>
  </article>
  <article class="service">
    <div class="thumb" role="img" aria-label="Red lawn mower on freshly cut grass" style="background:linear-gradient(100deg,#3a3a36 0%,#c8303c 35%,#a8293a 55%,#6fa03a 72%,#8fbf55 100%)"></div>
    <h2>Lawn Service</h2>
    <p>We service both residential and commercial properties.<br>We take pride in our Company, and this pride reflects<br>in the properties we maintain.</p>
    <a class="more" href="#">Learn more ›</a>
  </article>
  <article class="service">
    <div class="thumb" role="img" aria-label="Snow plow truck clearing a snowy street" style="background:linear-gradient(180deg,#9a8070 0%,#c9c9cb 35%,#eeeeef 70%,#d9d6d6 100%)"></div>
    <h2>Snow Removal Service</h2>
    <p>We service both residential and commercial properties.<br>We take pride in our Company, and this pride reflects<br>in the properties we maintain.</p>
    <a class="more" href="#">Learn more ›</a>
  </article>
</section>

<section class="featured">
  <h2>Featured</h2>
  <div class="pager">
    <span style="background:#aaa"><svg viewBox="0 0 16 15"><path d="M11 7.5H5M8 4L4.5 7.5 8 11" fill="none" stroke="#fff" stroke-width="2"/></svg></span>
    <span style="background:var(--green)"><svg viewBox="0 0 16 15"><path d="M5 7.5h6M8 4l3.5 3.5L8 11" fill="none" stroke="#fff" stroke-width="2"/></svg></span>
  </div>
  <div class="partners">
    <div class="partner"><i></i>Ardent Lawn</div>
    <div class="partner">Fernvale</div>
    <div class="partner">Hollis Yards</div>
    <div class="partner"><i style="border-radius:0"></i>Westbrook</div>
  </div>
</section>

<section class="cta">
  <p>If you have any questions regarding our service, please contact us, we’ll get back to you as soon as possible.</p>
  <a class="btn" href="#">Contact Us</a>
</section>

<footer class="footer">
  <div class="col" style="left:77px">
    <h3>What We Do</h3>
    <ul><li>Home</li><li>About us</li><li>New Business Registration</li><li>Business Login</li><li>Contact us</li></ul>
  </div>
  <div class="col" style="left:247px">
    <h3>Categories</h3>
    <ul><li>Landscape Service (2)</li><li>Lawn Service (2)</li><li>Snow Removal Service (1)</li><li>Tree Service (1)</li></ul>
  </div>
  <div class="col" style="left:417px">
    <h3>Social Bookmark</h3>
    <div class="social"><i></i><i></i><i></i><i></i><i></i><i></i><i></i></div>
  </div>
  <div class="col" style="left:587px">
    <h3>Contact Us</h3>
    <div class="contact-list">
      <div><svg viewBox="0 0 10 10"><path d="M2 0.5l2 2-1 1.3c.7 1.4 1.8 2.5 3.2 3.2l1.3-1 2 2-1.4 1.5C5 9.2 .8 5 .5 2z"/></svg>(555)010-4417</div>
      <div><svg viewBox="0 0 10 10"><path d="M1 3h8v6H1zM3 1h4v2H3z"/></svg>(555)010-4417</div>
      <div><svg viewBox="0 0 10 10"><path d="M0 2h10v6H0z"/></svg>hello@brindlemeadowyards.example</div>
    </div>
  </div>
  <div class="copyright">Copyrights 2013, All right reserved by Brindle Meadow Yards</div>
</footer>

</body>
</html>
```